BRAVO (Bright Regional Applied Vector Operations) Letter Head Design Project

Company Name: BRAVO (Bright Regional Applied Vector Operations) MFZ.
Office Address: Office No 718, Saffron Crest Block, Palmera Garden Quarter, Dubai, U.A.E
Company line of business:
1) Currently we have a POS solution for retail outlets like duty free shops, supermarkets, department stores etc... The solution is deployed in Harbourline Travel Retail on 350 POS and in Corniche Gate Travel Retail on 100 POS. So our main line of business is the deployment of this solution in retail outlets locally or regionally. We have already deployed the solution in India and Australia.
2) Integration of other third party POS systems with an online credit authorization netwotk in the UAE. This will enable POS applications to connect directly to the acquiring banks without needing an EFT terminal like Paxomat or Tallyrex. The credit card payment is completed at the POS.
3) Other solutions that are targeting retail outlets like mobile POS, queue busting solutions, stock taking solutions using hand held devices, transaction capture systems, etc...
4) Other IT services like support of call center solutions from Bluegrove Systems and development of new solutions as per customer requirements.
We need a letter head design for the company. We don't have any specific requirements in mind and we prefer to leave it up to the designers to come up with creative designs that will not be limited by any guidelines.
Updates
I have just uploaded all the files I received from my company logo designer. Please review and let me know if you need anything else. .
Dear All,
I have received very nice designs and I thank you for all the hard work you have put so far. I would like the letter head to have all the following company details:
Office Address: Office No 718, Saffron Crest Block, MFZ, Dubai UAE
P.O.Box: 58316 Dubai UAE
Tel Number:+971-4-5817730
Fax Number::+971-4-5817731
Website:www.bravomfz.ae
I would also like to represent the company details as a QRCode somewhere on the page, probably next to the company details if possible (as a trial).
In case you have included a butterfly in the middle of the page as part of your design, I prefer that it doesn't include any colors as colors might make reading the text on the page more difficult.
I don't want to have too many butterflies on the page. 2 are more than enough.
Can you also include a design for the continuation pages?
Thank you in advance and I look forward to receiving your creative designs.
Regards
Samir Odeyra

```html
<!DOCTYPE html>
<html lang="en">
<head>
<meta charset="utf-8">
<title>BRAVO Letterhead</title>
<link rel="stylesheet" href="https://fonts.googleapis.com/css2?family=Exo+2:wght@300;400&display=swap">
<style>
  :root {
    --paper: #ffffff;
    --ink: #1e1e1e;
    --ink-soft: #3a3a3a;
    --rule: #b9b9b9;
    --brand-blue: #0a6fb8;
    --blue-light: #1aa0dc;
    --blue-deep: #0b5a9e;
  }
  * { margin: 0; padding: 0; box-sizing: border-box; }
  html, body {
    width: 900px;
    height: 1200px;
    overflow: hidden;
    background: var(--paper);
  }
  .letterhead {
    position: relative;
    width: 900px;
    height: 1200px;
    background: var(--paper);
    font-family: "Exo 2", sans-serif;
    color: var(--ink);
  }
  .brand {
    position: absolute;
    left: 120px;
    top: 68px;
    display: flex;
    align-items: center;
    gap: 18px;
  }
  .brand-dot {
    width: 56px;
    height: 56px;
    border-radius: 50%;
    background: var(--brand-blue);
  }
  .brand-name {
    font-family: "Exo 2", sans-serif;
    font-weight: 400;
    font-size: 60px;
    line-height: 1;
    letter-spacing: 1px;
    color: var(--ink);
  }
  .header-rule {
    position: absolute;
    left: 540px;
    top: 64px;
    width: 1px;
    height: 78px;
    background: var(--rule);
  }
  .office-address {
    position: absolute;
    left: 563px;
    top: 76px;
    font-style: normal;
    font-weight: 300;
    font-size: 15.5px;
    line-height: 21px;
    color: var(--ink-soft);
  }
  .footer-band {
    position: absolute;
    left: 0;
    bottom: 0;
    width: 900px;
    height: 96px;
    background: linear-gradient(90deg, var(--blue-light), var(--blue-deep));
  }
</style>
</head>
<body>
  <main class="letterhead">
    <header>
      <div class="brand">
        <span class="brand-dot"></span>
        <span class="brand-name">BRAVO</span>
      </div>
      <div class="header-rule"></div>
      <address class="office-address">
        Office No 718, Saffron Crest Block,<br>
        Palmera Garden Quarter, Dubai, U.A.E
      </address>
    </header>

    <footer class="footer-band" role="img" aria-label="Decorative footer artwork in blue and lime tones"></footer>
  </main>
</body>
</html>
```